Business Card Design

We have our logo and everything in place. Looking to have a layout for our new business cards designed. These will be printed with a matte finish, possibly rounded corners, and looking to incorporate some cool spot UV layers into the design.

Ive uploaded the existing card front and back as well as our logo.

Card Size Will Be 3.5" x 2"

```html
<!DOCTYPE html>
<html lang="en">
<head>
<meta charset="utf-8">
<title>Hollowbrook Deck and Rail – Business Cards</title>
<link rel="stylesheet" href="https://fonts.googleapis.com/css2?family=Open+Sans:wght@400;600&display=swap">
<style>
  :root {
    --backdrop: #d3d3d3;
    --card-dark: #17232e;
    --card-mid: #2a3d4d;
    --ink: #ffffff;
    --ink-soft: #dfe6ec;
  }
  * { margin: 0; padding: 0; box-sizing: border-box; }
  html, body {
    width: 1200px;
    height: 900px;
    overflow: hidden;
    background: var(--backdrop);
    font-family: "Open Sans", Arial, sans-serif;
    color: var(--ink);
  }
  .canvas { position: relative; width: 1200px; height: 900px; }
  .card {
    position: absolute;
    top: 307px;
    width: 439px;
    height: 270px;
    border-radius: 10px;
    background: radial-gradient(ellipse at 60% 20%, var(--card-mid) 0%, var(--card-dark) 75%);
  }
  .card--front { left: 150px; }
  .card--back { left: 609px; }

  .wordmark {
    position: absolute;
    font-weight: 600;
    color: var(--ink);
    white-space: nowrap;
    text-align: center;
  }
  .card--front .wordmark { right: 26px; top: 62px; font-size: 26px; }
  .card--back .wordmark { left: 0; right: 0; top: 112px; font-size: 34px; }

  .holder { position: absolute; left: 28px; top: 142px; }
  .holder__name { font-size: 14.5px; font-weight: 600; line-height: 18px; }
  .holder__title { font-size: 12px; line-height: 16px; color: var(--ink-soft); }

  .contacts { position: absolute; left: 28px; top: 194px; list-style: none; }
  .contacts li {
    display: flex; align-items: center;
    font-size: 11.5px; line-height: 16px; color: var(--ink-soft);
  }
  .contacts svg { width: 9px; height: 9px; margin-right: 9px; fill: var(--ink-soft); }
</style>
</head>
<body>
<main class="canvas">
  <section class="card card--front" aria-label="Card front">
    <div class="wordmark">Hollowbrook</div>
    <div class="holder">
      <p class="holder__name">Daniel Brooks</p>
      <p class="holder__title">President</p>
    </div>
    <ul class="contacts">
      <li>
        <svg viewBox="0 0 10 10" aria-hidden="true"><path d="M2 0.5 L3.6 2.6 L2.8 3.6 Q4 6 6.4 7.2 L7.4 6.4 L9.5 8 L8.4 9.5 Q4.5 9.5 0.5 1.6 Z"/></svg>
        403.555.0187
      </li>
      <li>
        <svg viewBox="0 0 10 10" aria-hidden="true"><path d="M0.5 2 H9.5 V8 H0.5 Z M1 2.4 L5 5.4 L9 2.4" stroke="#17232e" stroke-width="0.8"/></svg>
        hollowbrookdeck@gmail.com
      </li>
      <li>
        <svg viewBox="0 0 10 10" aria-hidden="true"><circle cx="5" cy="5" r="4.5"/></svg>
        www.hollowbrookdeck.com
      </li>
    </ul>
  </section>

  <section class="card card--back" aria-label="Card back">
    <div class="wordmark">Hollowbrook</div>
  </section>
</main>
</body>
</html>
```